California, rapidly growing Insurance Agency needs logo and letterhead design

we need a logo design and letterhead for an insurance company that specialize in providing businesses with insurance (workers comp , group health insurance, business insurance). I would like to see designs with a professional layout that use dark rich blues, and maybe some lighter blues mixed in. Also open to using grey and red tones. The design should communicate professional, yet current day feel (not too old/stuff or boring feel).
Updates

The company name is “Dovrel Insurance Services” If possible , would like to see a letterhead option with tag line worked in somewhere as “insurance specialist for over 45 years” Thank you!!!!

Target Market(s)

We insure businesses, do would like professional look with out being too stuffy or boring

Industry/Entity Type

Insurance Agency

Logo Text

Maybe “We make Insurance easy”

Font styles to use
Serif

Colors
3176b5
0993cd
f04b51

Requirements
Nice to have
• Would like to have rich dark blues and light mixed or also open to grey and
• Red color scheme
Should not have
• We target higher end clients, so would like to stay away from
• Any type of anime graphic

```html
<!DOCTYPE html>
<html lang="en">
<head>
<meta charset="utf-8">
<title>Dovrel Insurance Services — Letterhead</title>
<link href="https://fonts.googleapis.com/css2?family=Inter:wght@400;600&display=swap" rel="stylesheet">
<style>
  :root {
    --backdrop: #bdbcc3;
    --paper: #f9f9f9;
    --ink: #3f4249;
    --ink-soft: #4a4d54;
    --rule: #8a8c92;
    --brand-blue: #0a5cc2;
  }
  * { margin: 0; padding: 0; box-sizing: border-box; }
  html, body {
    width: 1200px;
    height: 1161px;
    overflow: hidden;
    background: var(--backdrop);
    font-family: "Inter", Arial, sans-serif;
    color: var(--ink);
  }
  .letterhead {
    position: absolute;
    left: 225px;
    top: 105px;
    width: 743px;
    height: 958px;
    background: var(--paper);
  }
  .brand {
    position: absolute;
    right: 62px;
    top: 178px;
    display: flex;
    align-items: center;
    gap: 10px;
  }
  .brand-mark {
    width: 22px;
    height: 22px;
    background: var(--brand-blue);
  }
  .brand-name {
    font-size: 21px;
    font-weight: 600;
    letter-spacing: 0.01em;
    color: var(--ink);
    white-space: nowrap;
  }
  .footer-rule {
    position: absolute;
    left: 61px;
    right: 62px;
    top: 884px;
    height: 1px;
    background: var(--rule);
  }
  .contact {
    position: absolute;
    left: 61px;
    top: 898px;
    font-size: 9px;
    line-height: 11.5px;
    color: var(--ink-soft);
  }
  .tagline {
    position: absolute;
    right: 60px;
    top: 903px;
    font-size: 13px;
    letter-spacing: 0.01em;
    color: var(--ink);
    white-space: nowrap;
  }
</style>
</head>
<body>
  <main class="letterhead">
    <header class="brand">
      <span class="brand-mark" aria-hidden="true"></span>
      <span class="brand-name">DOVREL INSURANCE SERVICES</span>
    </header>

    <div class="footer-rule"></div>
    <address class="contact" style="font-style: normal;">
      2280 N. Harbor View Drive, Seal Cove, CA 90412<br>
      Phone: 555.204.7100 · Fax: 555.204.7161
    </address>
    <p class="tagline">INSURANCE SPECIALIST FOR OVER 45 YEARS</p>
  </main>
</body>
</html>
```